Glofarvik - Start-up company selling electricity

Hello let me tell you about Glofarvik.

Glofarvik is start-up company selling electricity in Iceland. The operations of the company consist of making power usage forecasts for our customers, purchasing the electricity wholesale from the energy producers, and selling the electricity to the consumer. We are focused on tech by using optimization and machine learning to minimize electricity prices to our customers. Our marketing strategy is to portray a tech company mindset and to show dedication to driving down the electricity price on the market.

We need your help to make our website pop. Possible concepts to work with are as follows:

- Iceland the land of ice and fire
- Green energy
- Innovation
- Tech and data science

Link to our website: https://prufa.glofarvik-example.is/
We are open to ideas.
Thank you!

Target Market(s)

Electricity consumers both homes and companies.

Number of Pages Required

1 page

Font styles to use
Serif
Sans Serif

```html
<!DOCTYPE html>
<html lang="is">
<head>
<meta charset="utf-8">
<title>Glofarvik – Sama rafmagn, bara ódýrara</title>
<link rel="stylesheet" href="https://fonts.googleapis.com/css2?family=Poppins:wght@400&family=Ubuntu:wght@500&family=Source+Sans+3:wght@400;600&display=swap">
<style>
  :root {
    --canvas: #f4f5f9;
    --page: #ffffff;
    --ink: #24262b;
    --body-ink: #2d2f33;
    --coral: #ec6670;
    --blue: #3a9bf5;
    --grad-start: #e96a74;
    --grad-mid: #9a7ab8;
    --grad-end: #2f8ff5;
    --night-top: #101620;
    --night-mid: #1d2633;
    --night-glow: #5a4650;
    --night-ground: #0d0f16;
    --chevron: #8b8d94;
  }
  * { box-sizing: border-box; margin: 0; padding: 0; }
  html, body {
    width: 1200px; height: 849px; overflow: hidden;
    background: var(--canvas);
  }
  .landing {
    position: absolute; left: 0; top: 88px;
    width: 1200px; height: 673px;
    background: var(--page);
    border-radius: 8px;
    overflow: hidden;
  }
  .brand {
    position: absolute; left: 53px; top: 22px;
    display: flex; align-items: center; gap: 7px;
    font-family: "Poppins", sans-serif; font-weight: 400;
    font-size: 15px; color: var(--ink);
  }
  .brand-dot {
    width: 14px; height: 14px; border-radius: 50%;
    background: var(--coral);
  }
  .hero-visual {
    position: absolute; left: 600px; top: 0;
    width: 600px; height: 673px;
    border-bottom-left-radius: 180px;
    background:
      radial-gradient(ellipse 70% 35% at 45% 100%, var(--night-glow) 0%, transparent 70%),
      linear-gradient(180deg, var(--night-top) 0%, var(--night-mid) 55%, #3a3440 80%, var(--night-ground) 100%);
  }
  .main-nav {
    position: absolute; top: 27px; left: 0; width: 1200px; height: 20px;
    font-family: "Source Sans 3", sans-serif; font-weight: 600;
    font-size: 14px; letter-spacing: 0.5px; color: #ffffff;
  }
  .main-nav a { position: absolute; color: inherit; text-decoration: none; }
  .nav-about { left: 707px; }
  .nav-faq { left: 867px; }
  .nav-terms { left: 1026px; }
  .headline {
    position: absolute; left: 140px; top: 198px;
    font-family: "Ubuntu", sans-serif; font-weight: 500;
    font-size: 50px; line-height: 57px; letter-spacing: 0.5px;
    color: var(--ink);
  }
  .headline-accent {
    display: inline-block;
    letter-spacing: 2px;
    background: linear-gradient(90deg, var(--grad-start) 0%, var(--grad-mid) 50%, var(--grad-end) 100%);
    -webkit-background-clip: text; background-clip: text;
    color: transparent;
  }
  .intro {
    position: absolute; left: 140px; top: 345px; width: 400px;
    font-family: "Source Sans 3", sans-serif; font-weight: 400;
    font-size: 18.5px; line-height: 25px; letter-spacing: 0.6px;
    color: var(--body-ink);
  }
  .audience-choice {
    position: absolute; left: 140px; top: 462px;
    display: flex; gap: 10px;
  }
  .pill {
    width: 136px; height: 47px; border-radius: 24px;
    display: flex; align-items: center; justify-content: center;
    font-family: "Source Sans 3", sans-serif; font-weight: 600;
    font-size: 16px; letter-spacing: 0.6px; color: #ffffff;
    text-decoration: none;
  }
  .pill-business { background: var(--coral); }
  .pill-home { background: var(--blue); }
  .scroll-hint { position: absolute; left: 144px; top: 612px; }
</style>
</head>
<body>
  <main class="landing">
    <div class="brand"><span class="brand-dot"></span>Glofarvik</div>

    <div class="hero-visual" role="img" aria-label="Ljósmynd: maður á hæð beinir vasaljósi upp í stjörnubjartan næturhimin"></div>

    <nav class="main-nav">
      <a class="nav-about" href="#">Um Glofarvik</a>
      <a class="nav-faq" href="#">Spurt &amp; Svarað</a>
      <a class="nav-terms" href="#">Viðskiptaskilmálar</a>
    </nav>

    <h1 class="headline">Sama rafmagn<br><span class="headline-accent">Bara ódýrara!</span></h1>

    <p class="intro">Glofarvik notar gervigreind, gagnavísindi og sjálfvirkni til að lágmarka kostnað og stuðla að okrujöfnuði</p>

    <div class="audience-choice">
      <a class="pill pill-business" href="#">Fyrirtæki</a>
      <a class="pill pill-home" href="#">Heimili</a>
    </div>

    <svg class="scroll-hint" width="38" height="14" viewBox="0 0 38 14" aria-hidden="true">
      <polyline points="1,2 19,12 37,2" fill="none" stroke="var(--chevron)" stroke-width="1.4"/>
    </svg>
  </main>
</body>
</html>
```